Lottery Scratchcard templates for charities

We produce scratch cards for charities to sell to their supporters to raise funds.

We need a set of templates which can be re-used for different clients by simply replacing text, logo, prizes and a potentially a picture.

One of the templates can be plain simply using block colours
One can use generic images like a treasure chests which indicate money can be won
One templates can feature space for a photograph which can be easily replaced and updated depending on the client - example, a picture of a dog for a dog charity can easily be replaced by a picture of a football team for a club.

Target Market(s)

People who support a charity and the charities themselves

Industry/Entity Type

Charity

Colors

Designer to choose colors to be used in the design.

Requirements
Must have
• Every card will need space for:
• - The charity's logo
• - our logo
• - a panel which can be scratched off (use a plain silver, but can have an image printed on top in black only)
• - information about how to win (this can be lorem ipsum text)
• - Prizes (usually 4 or 5 prize levels of £100, £50, £10, £1)
• - Price: £1 and/or Just £1 to play
• - Small print - "Please play responsibly www.KeelbrookTrust.org."
• minimum size 4pt
• Paper size: A7, print ready
• Format: Adobe InDesign, fully editable
• Vector illustrations/design elements

```html
<!DOCTYPE html>
<html lang="en">
<head>
<meta charset="utf-8">
<title>Charity Scratchcard Templates</title>
<link rel="stylesheet" href="https://fonts.googleapis.com/css2?family=Anton&family=Noto+Serif&family=Roboto:wght@500;700&family=Roboto+Condensed:ital,wght@0,700;1,700&display=swap">
<style>
  :root {
    --page: #dcdcdc;
    --royal: #0a4fb4;
    --royal-dark: #0a3f95;
    --sky: #3d8fe0;
    --glow: #dcefff;
    --white: #ffffff;
    --silver: #c4c4c4;
    --silver-edge: #9a9a9a;
    --ink: #111111;
    --navy: #0b2a78;
    --grass: #3ee03a;
    --grass-dark: #2bb52a;
    --photo-a: #8d9bb0;
    --photo-b: #e6e2da;
    --notes-a: #e9c6c0;
    --notes-b: #f6efe8;
  }
  * { box-sizing: border-box; margin: 0; padding: 0; }
  html, body { width: 786px; height: 1200px; overflow: hidden; background: var(--page); }
  .canvas { position: relative; width: 786px; height: 1200px; }

  .card {
    position: absolute; left: 182px; width: 422px; height: 307px; overflow: hidden;
    background: var(--royal); font-family: "Roboto", sans-serif; color: var(--white);
    box-shadow: 14px 14px 22px rgba(0,0,0,.45);
  }
  .card--photo { top: 86px; background: radial-gradient(ellipse at 30% 60%, #2a74d6 0%, var(--royal) 70%); }
  .card--prize { top: 446px; background: radial-gradient(ellipse 60% 55% at 50% 50%, var(--glow) 0%, #8cc4f4 30%, var(--sky) 65%, #2a6fcf 100%); }
  .card--plain { top: 806px; background: radial-gradient(ellipse 45% 50% at 50% 58%, var(--glow) 0%, #4d98e4 45%, var(--royal) 85%); }

  .frame { position: absolute; border: 2px solid var(--white); }
  .hill, .band { position: absolute; left: 0; bottom: 0; width: 422px; height: 60px; }

  .logo { position: absolute; font-weight: 500; line-height: .92; text-transform: uppercase; color: var(--white); white-space: nowrap; }
  .logo--ours { font-size: 25px; }
  .logo--charity .small { display: block; font-size: 16px; }
  .logo--charity .large { display: block; font-size: 26px; }

  .how-to-win { position: absolute; line-height: 1.15; white-space: nowrap; }
  .how-to-win--serif { font-family: "Noto Serif", serif; font-size: 17px; letter-spacing: -.2px; color: var(--white); text-align: center; }
  .how-to-win--outlined { font-family: "Noto Serif", serif; font-size: 17px; letter-spacing: -.2px; color: var(--navy); -webkit-text-stroke: 3px var(--white); paint-order: stroke fill; text-align: right; }
  .how-to-win--condensed { font-family: "Anton", sans-serif; font-size: 22px; color: #1d4fc0; -webkit-text-stroke: 3px var(--white); paint-order: stroke fill; text-align: left; line-height: 1.15; letter-spacing: -.3px; }

  .prize { position: absolute; font-family: "Anton", sans-serif; color: #f4f4f4; -webkit-text-stroke: 3px #1a1a1a; paint-order: stroke fill; white-space: nowrap; line-height: 1; }
  .prize .lead { font-size: 21px; }
  .prize .amount { font-size: 35px; }

  .price-badge { position: absolute; width: 70px; height: 70px; }

  .scratch {
    position: absolute; width: 47px; height: 47px; border-radius: 5px;
    background: linear-gradient(#d2d2d2, var(--silver)); border: 1px solid var(--silver-edge);
    display: flex; align-items: center; justify-content: center;
    font-family: "Roboto", sans-serif; font-weight: 700; font-size: 30px; color: var(--ink);
  }
  .scratch--wide { width: 61px; height: 40px; border: 2px solid var(--royal-dark); border-radius: 6px; }
  .heart { position: absolute; width: 67px; height: 62px; }

  .media { position: absolute; }
  .media--pets { left: 22px; top: 150px; width: 256px; height: 132px; border-radius: 40% 40% 10% 10%; background: radial-gradient(ellipse at 55% 55%, var(--photo-b) 0%, var(--photo-a) 55%, rgba(141,155,176,0) 75%); }
  .media--notes { left: 114px; top: 62px; width: 208px; height: 196px; background: radial-gradient(ellipse at 50% 50%, var(--notes-b) 0%, var(--notes-a) 50%, rgba(233,198,192,0) 75%); }

  .small-print { position: absolute; font-family: "Roboto Condensed", sans-serif; font-weight: 700; font-size: 10.5px; line-height: 1.2; color: var(--white); white-space: nowrap; }
  .small-print .url { display: block; font-family: "Roboto", sans-serif; font-weight: 500; font-size: 6px; }
  .small-print--right { right: 30px; top: 220px; text-align: right; }
  .small-print--center { left: 0; width: 422px; top: 262px; text-align: center; }
  .small-print--italic { font-style: italic; }
</style>
</head>
<body>
<main class="canvas">

  <!-- Template 1: photograph -->
  <section class="card card--photo">
    <div class="frame" style="left:18px;top:18px;width:385px;height:290px;"></div>
    <div class="media media--pets" role="img" aria-label="Replaceable photograph: a kitten and a puppy touching noses"></div>
    <svg class="hill" viewBox="0 0 422 60" aria-hidden="true">
      <path d="M0 22 Q210 -8 422 14 L422 60 L0 60Z" fill="var(--grass)"/>
      <path d="M0 22 Q210 -8 422 14 L422 20 Q210 0 0 28Z" fill="var(--grass-dark)" opacity=".5"/>
    </svg>
    <div class="logo logo--ours" style="left:30px;top:30px;">Your<br>Logo</div>
    <div class="logo logo--charity" style="left:107px;top:32px;"><span class="small">Charity</span><span class="large">Logo</span></div>
    <p class="how-to-win how-to-win--serif" style="left:198px;top:32px;width:196px;">Lorem Ipsum is simply<br>dummy text</p>
    <svg class="price-badge" style="left:31px;top:83px;" viewBox="0 0 70 70" aria-label="Just £1 to play">
      <circle cx="35" cy="35" r="34" fill="var(--royal)" stroke="var(--white)" stroke-width="1.5"/>
      <path id="ring1" d="M35 8 a27 27 0 1 1 -0.1 0" fill="none"/>
      <text font-family="Roboto, sans-serif" font-size="6.5" fill="var(--white)"><textPath href="#ring1">Just £1 to play · Just £1 to play · Just £1 to play ·</textPath></text>
      <text x="35" y="44" text-anchor="middle" font-family="Roboto, sans-serif" font-weight="700" font-size="25" fill="var(--white)">£1</text>
    </svg>
    <div class="prize" style="left:112px;top:89px;"><span class="lead">WIN UPTO</span> <span class="amount">£100</span></div>
    <div class="scratch" style="left:284px;top:90px;">£</div>
    <div class="scratch" style="left:345px;top:90px;">£</div>
    <div class="scratch" style="left:284px;top:150px;">£</div>
    <div class="scratch" style="left:345px;top:150px;">£</div>
    <p class="small-print small-print--right">Please play responsibly<span class="url">www.KeelbrookTrust.org</span></p>
  </section>

  <!-- Template 2: prize imagery -->
  <section class="card card--prize">
    <div class="media media--notes" role="img" aria-label="Illustration of banknotes flying outwards"></div>
    <svg class="band" viewBox="0 0 422 60" aria-hidden="true" style="height:50px;">
      <path d="M0 22 Q210 -4 422 22 L422 60 L0 60Z" fill="#1e63c6"/>
    </svg>
    <div class="logo logo--ours" style="left:28px;top:26px;">Your<br>Logo</div>
    <div class="logo logo--charity" style="left:102px;top:28px;"><span class="small" style="font-size:14px;">Charity</span><span class="large" style="font-size:21px;">Logo</span></div>
    <p class="how-to-win how-to-win--outlined" style="left:190px;top:26px;width:196px;">Lorem Ipsum is simply<br><span style="padding-right:46px;">dummy text</span></p>
    <svg class="price-badge" style="left:29px;top:101px;" viewBox="0 0 70 70" aria-label="Just £1 to play">
      <circle cx="35" cy="35" r="34" fill="#1553b8" stroke="var(--white)" stroke-width="1.5"/>
      <path id="ring2" d="M35 8 a27 27 0 1 1 -0.1 0" fill="none"/>
      <text font-family="Roboto, sans-serif" font-size="6.5" fill="var(--white)"><textPath href="#ring2">Just £1 to play · Just £1 to play · Just £1 to play ·</textPath></text>
      <text x="35" y="44" text-anchor="middle" font-family="Roboto, sans-serif" font-weight="700" font-size="25" fill="var(--white)">£1</text>
    </svg>
    <div class="prize" style="left:28px;top:190px;color:#9fc9f5;-webkit-text-stroke-color:var(--navy);"><span class="lead">WIN UPTO</span></div>
    <div class="prize" style="left:39px;top:214px;color:#9fc9f5;-webkit-text-stroke-color:var(--navy);"><span class="amount" style="font-size:32px;">£100</span></div>
    <div class="scratch scratch--wide" style="left:326px;top:77px;">£</div>
    <div class="scratch scratch--wide" style="left:326px;top:121px;">£</div>
    <div class="scratch scratch--wide" style="left:326px;top:166px;">£</div>
    <div class="scratch scratch--wide" style="left:326px;top:210px;">£</div>
    <p class="small-print small-print--center small-print--italic" style="top:260px;">Please play responsibly<span class="url" style="font-style:normal;">www.KeelbrookTrust.org</span></p>
  </section>

  <!-- Template 3: plain block colour -->
  <section class="card card--plain">
    <div class="frame" style="left:23px;top:23px;width:374px;height:290px;"></div>
    <svg class="hill" viewBox="0 0 422 60" aria-hidden="true">
      <path d="M0 26 Q210 -6 422 20 L422 60 L0 60Z" fill="var(--grass)"/>
      <path d="M0 26 Q210 -6 422 20 L422 26 Q210 2 0 32Z" fill="var(--grass-dark)" opacity=".5"/>
    </svg>
    <div class="logo logo--ours" style="left:50px;top:28px;font-size:27px;">Our<br>Logo</div>
    <div class="logo logo--charity" style="left:132px;top:30px;"><span class="small">Charity</span><span class="large" style="font-size:27px;">Logo</span></div>
    <p class="how-to-win how-to-win--condensed" style="left:50px;top:76px;">Lorem Ipsum is simply<br><span style="padding-left:48px;">dummy text</span></p>
    <svg class="price-badge" style="left:299px;top:36px;width:78px;height:78px;" viewBox="0 0 70 70" aria-label="Just £1 to play">
      <circle cx="35" cy="35" r="34" fill="var(--royal)" stroke="var(--white)" stroke-width="1.5"/>
      <path id="ring3" d="M35 8 a27 27 0 1 1 -0.1 0" fill="none"/>
      <text font-family="Roboto, sans-serif" font-size="6.5" fill="var(--white)"><textPath href="#ring3">Just £1 to play · Just £1 to play · Just £1 to play ·</textPath></text>
      <text x="35" y="44" text-anchor="middle" font-family="Roboto, sans-serif" font-weight="700" font-size="25" fill="var(--white)">£1</text>
    </svg>
    <svg class="heart" style="left:46px;top:131px;" viewBox="0 0 67 62" aria-label="Scratch panel">
      <path d="M33.5 59 C10 42 2 30 2 18 C2 8 10 2 19 2 C26 2 31 6 33.5 11 C36 6 41 2 48 2 C57 2 65 8 65 18 C65 30 57 42 33.5 59Z" fill="var(--silver)" stroke="#5d8fd6" stroke-width="2.5"/>
      <text x="33.5" y="40" text-anchor="middle" font-family="Roboto, sans-serif" font-weight="700" font-size="28" fill="var(--ink)">£</text>
    </svg>
    <svg class="heart" style="left:132px;top:131px;" viewBox="0 0 67 62" aria-label="Scratch panel">
      <path d="M33.5 59 C10 42 2 30 2 18 C2 8 10 2 19 2 C26 2 31 6 33.5 11 C36 6 41 2 48 2 C57 2 65 8 65 18 C65 30 57 42 33.5 59Z" fill="var(--silver)" stroke="#2a3fb0" stroke-width="2.5"/>
      <text x="33.5" y="40" text-anchor="middle" font-family="Roboto, sans-serif" font-weight="700" font-size="28" fill="var(--ink)">£</text>
    </svg>
    <svg class="heart" style="left:219px;top:131px;" viewBox="0 0 67 62" aria-label="Scratch panel">
      <path d="M33.5 59 C10 42 2 30 2 18 C2 8 10 2 19 2 C26 2 31 6 33.5 11 C36 6 41 2 48 2 C57 2 65 8 65 18 C65 30 57 42 33.5 59Z" fill="var(--silver)" stroke="#1d5fbf" stroke-width="2.5"/>
      <text x="33.5" y="40" text-anchor="middle" font-family="Roboto, sans-serif" font-weight="700" font-size="28" fill="var(--ink)">£</text>
    </svg>
    <svg class="heart" style="left:305px;top:131px;" viewBox="0 0 67 62" aria-label="Scratch panel">
      <path d="M33.5 59 C10 42 2 30 2 18 C2 8 10 2 19 2 C26 2 31 6 33.5 11 C36 6 41 2 48 2 C57 2 65 8 65 18 C65 30 57 42 33.5 59Z" fill="var(--silver)" stroke="#3a2fb0" stroke-width="2.5"/>
      <text x="33.5" y="40" text-anchor="middle" font-family="Roboto, sans-serif" font-weight="700" font-size="28" fill="var(--ink)">£</text>
    </svg>
    <div class="prize" style="left:114px;top:203px;"><span class="lead">WIN UPTO</span> <span class="amount" style="font-size:42px;">£100</span></div>
    <p class="small-print small-print--center" style="top:264px;">Please play responsibly<span class="url">www.KeelbrookTrust.org</span></p>
  </section>

</main>
</body>
</html>
```